Business Card Design for Venture Kite

Venture Kite is a pro bono student consultancy service offered by Corvala KTRB to social start ups and enterprises. We provide consulting services with expertise in areas such as Marketing, IT, Business Strategy and Innovation.
I have attached\ the Venture Kite Logo here for your perusal.
Industry/Entity Type
Business
Contact Information for Business Card
Name: Ha Min Park Name: Thomas Leung
Role: Project Leader Role: Vice Project Leader
M:0477203941 M: 0479352806
E: ha-min.park@corvalaktrb.org E: thomas.leung@corvalaktrb.org
W: www.corvalaktrb.org W: www.corvalaktrb.org

```html
<!DOCTYPE html>
<html lang="en">
<head>
<meta charset="utf-8">
<title>Venture Kite — Business Cards</title>
<link rel="stylesheet" href="https://fonts.googleapis.com/css2?family=Chakra+Petch:wght@700&family=Lato:wght@400&display=swap">
<style>
  :root {
    --orange: #ff7a00;
    --ink: #111111;
    --paper: #ffffff;
    --edge: #3a3a3a;
  }
  * { margin: 0; padding: 0; box-sizing: border-box; }
  html, body { width: 1200px; height: 717px; overflow: hidden; background: var(--paper); }
  .sheet { position: relative; width: 1200px; height: 717px; }
  .card {
    position: absolute; width: 572px; height: 346px;
    background: var(--paper); border: 1px solid var(--edge); overflow: hidden;
  }
  .card--front-a { left: 0; top: 0; }
  .card--back-a { left: 628px; top: 0; }
  .card--front-b { left: 0; top: 371px; }
  .card--back-b { left: 628px; top: 371px; }
  .card__stripes { position: absolute; inset: 0; width: 100%; height: 100%; }
  .card__stripes polygon { fill: var(--orange); }
  .brand {
    position: absolute; left: 0; right: 0; top: 128px;
    text-align: center; color: var(--ink);
    font-family: "Chakra Petch", sans-serif; font-weight: 700;
    font-size: 48px; line-height: 1.15; letter-spacing: 1px;
    text-transform: uppercase;
  }
  .person { position: absolute; left: 62px; top: 64px; }
  .person__name {
    font-family: "Chakra Petch", sans-serif; font-weight: 700;
    font-size: 31px; color: var(--ink); letter-spacing: 0.5px; line-height: 1.1;
  }
  .person__role {
    font-family: Arial, Helvetica, sans-serif; font-style: italic;
    font-size: 17px; color: var(--ink); margin-top: 2px;
  }
  .contacts {
    position: absolute; left: 62px; top: 212px; list-style: none;
    font-family: "Lato", sans-serif; font-size: 16.5px; color: var(--ink);
  }
  .contacts li { display: flex; align-items: center; height: 23.5px; }
  .contacts svg { width: 14px; height: 14px; margin-right: 12px; flex: none; }
  .icon-fill { fill: var(--ink); }
  .icon-line { fill: none; stroke: var(--ink); stroke-width: 1.4; }
</style>
</head>
<body>
<main class="sheet">

  <section class="card card--front-a">
    <svg class="card__stripes" viewBox="0 0 572 346" aria-hidden="true">
      <polygon points="0,0 108,0 0,188"/>
      <polygon points="114,0 123,0 0,208 0,194"/>
      <polygon points="448,346 457,346 572,168 572,154"/>
      <polygon points="463,346 572,346 572,177"/>
    </svg>
    <h1 class="brand">Venture Kite</h1>
  </section>

  <section class="card card--back-a">
    <svg class="card__stripes" viewBox="0 0 572 346" aria-hidden="true">
      <polygon points="464,0 476,0 322,346 310,346"/>
      <polygon points="485,0 572,0 572,76 452,346 328,346"/>
      <polygon points="460,346 472,346 572,121 572,94"/>
    </svg>
    <div class="person">
      <h2 class="person__name">Thomas Leung</h2>
      <p class="person__role">Vice Project Leader</p>
    </div>
    <ul class="contacts">
      <li><svg viewBox="0 0 14 14" aria-hidden="true"><rect class="icon-line" x="4" y="1" width="6.5" height="12" rx="1.2"/><line class="icon-line" x1="6.3" y1="11" x2="8.2" y2="11"/></svg>0479352806</li>
      <li><svg viewBox="0 0 14 14" aria-hidden="true"><rect class="icon-fill" x="1.5" y="3.5" width="11" height="7.5"/><polyline points="1.5,3.8 7,8 12.5,3.8" fill="none" stroke="#fff" stroke-width="1"/></svg>thomas.leung@corvalaktrb.org</li>
      <li><svg viewBox="0 0 14 14" aria-hidden="true"><circle class="icon-line" cx="7" cy="7" r="5.6"/><ellipse class="icon-line" cx="7" cy="7" rx="2.4" ry="5.6"/><line class="icon-line" x1="1.4" y1="7" x2="12.6" y2="7"/></svg>www.corvalaktrb.org</li>
    </ul>
  </section>

  <section class="card card--front-b">
    <svg class="card__stripes" viewBox="0 0 572 346" aria-hidden="true">
      <polygon points="0,0 108,0 0,188"/>
      <polygon points="114,0 123,0 0,208 0,194"/>
      <polygon points="448,346 457,346 572,168 572,154"/>
      <polygon points="463,346 572,346 572,177"/>
    </svg>
    <h1 class="brand">Venture Kite</h1>
  </section>

  <section class="card card--back-b">
    <svg class="card__stripes" viewBox="0 0 572 346" aria-hidden="true">
      <polygon points="464,0 476,0 322,346 310,346"/>
      <polygon points="485,0 572,0 572,76 452,346 328,346"/>
      <polygon points="460,346 472,346 572,121 572,94"/>
    </svg>
    <div class="person">
      <h2 class="person__name">Ha Min Park</h2>
      <p class="person__role">Project Leader</p>
    </div>
    <ul class="contacts">
      <li><svg viewBox="0 0 14 14" aria-hidden="true"><rect class="icon-line" x="4" y="1" width="6.5" height="12" rx="1.2"/><line class="icon-line" x1="6.3" y1="11" x2="8.2" y2="11"/></svg>0477203941</li>
      <li><svg viewBox="0 0 14 14" aria-hidden="true"><rect class="icon-fill" x="1.5" y="3.5" width="11" height="7.5"/><polyline points="1.5,3.8 7,8 12.5,3.8" fill="none" stroke="#fff" stroke-width="1"/></svg>ha-min.park@corvalaktrb.org</li>
      <li><svg viewBox="0 0 14 14" aria-hidden="true"><circle class="icon-line" cx="7" cy="7" r="5.6"/><ellipse class="icon-line" cx="7" cy="7" rx="2.4" ry="5.6"/><line class="icon-line" x1="1.4" y1="7" x2="12.6" y2="7"/></svg>www.corvalaktrb.org</li>
    </ul>
  </section>

</main>
</body>
</html>
```